Attention grabbing 6x9 postcard

We are looking to have an attention grabbing post card that be sent out to homeowners from our roofing company Olum Roofing. the concept is that on the front it will say something like (STOP THE KNOCKING!
Tired of roofers knocking on your door? Contact us because we value your time as much as you value the roof over your head."
Olum Roofing
OlumRoofing.com
877.612.OLUM
info@olumroofing.com

Please feel free to come up with something very creative. Once we pick the final design we will provide the copy.

```html
<!DOCTYPE html>
<html lang="en">
<head>
<meta charset="utf-8">
<title>Olum Roofing Postcard</title>
<link rel="stylesheet" href="https://fonts.googleapis.com/css2?family=Oswald:wght@600;700&family=Montserrat:ital,wght@1,800&family=Poppins:wght@400;500&display=swap">
<style>
:root{
  --yellow:#e8b031;
  --black:#1f1d1d;
  --white:#ffffff;
  --stripe:#dcdcdc;
  --page:#e6e6e6;
  --stamp:#a7a7a9;
}
*{margin:0;padding:0;box-sizing:border-box}
html,body{width:1200px;height:1117px;overflow:hidden;background:var(--page)}
.card{position:absolute;left:195px;width:810px;height:525px;background:var(--white);overflow:hidden;box-shadow:0 2px 10px rgba(0,0,0,.12)}
.card-front{top:20px}
.card-back{top:572px}
.card svg.shapes{position:absolute;inset:0;width:810px;height:525px}
.brand{position:absolute;left:52px;top:30px;display:flex;align-items:center;gap:18px}
.brand-dot{width:46px;height:46px;border-radius:50%;background:var(--yellow)}
.brand-name{font-family:'Oswald',sans-serif;font-weight:600;font-size:44px;line-height:1;color:var(--black);text-transform:uppercase}
.headline{position:absolute;left:48px;font-family:'Oswald',sans-serif;font-weight:700;text-transform:uppercase;line-height:1}
.headline-stop{top:154px;font-size:86px;color:var(--yellow)}
.headline-knock{top:250px;font-size:96px;color:var(--black)}
.tagline{position:absolute;left:50px;top:372px;font-family:'Montserrat',sans-serif;font-style:italic;font-weight:800;font-size:21px;line-height:1.25;color:var(--black);text-transform:uppercase}
.phone{position:absolute;display:flex;align-items:center;gap:14px;font-family:'Poppins',sans-serif;font-weight:500;color:var(--white);font-size:34px}
.phone svg{width:36px;height:36px}
.front-phone{left:48px;top:460px}
.value-note{position:absolute;left:455px;width:355px;top:435px;text-align:center;font-family:'Poppins',sans-serif;font-size:17px;line-height:1.22;color:var(--black)}
.contact-title{position:absolute;left:54px;top:20px;font-family:'Oswald',sans-serif;font-weight:600;font-size:54px;line-height:1.1;text-transform:uppercase;color:var(--yellow)}
.contact-title span{color:var(--black)}
.work-grid{position:absolute;left:54px;top:92px;width:330px;display:grid;grid-template-columns:repeat(3,1fr);gap:6px}
.work-tile{height:106px;border:3px solid var(--black)}
.tile-a{background:linear-gradient(#6f8fbf,#8a6a4a)}
.tile-b{background:linear-gradient(135deg,#4a7db8,#5fa0dd 55%,#3f6d3a)}
.tile-c{background:linear-gradient(#7f8c95,#9a9488)}
.tile-d{background:linear-gradient(#9aa3ad,#5c6169)}
.tile-e{background:linear-gradient(#6e8db5,#4a4d66)}
.tile-f{background:linear-gradient(135deg,#3d5a3a,#c88a55)}
.caption{position:absolute;left:20px;width:380px;top:324px;text-align:center;font-family:'Poppins',sans-serif;font-size:17px;line-height:1.2;color:var(--black)}
.back-phone{left:54px;top:394px}
.contact-line{position:absolute;left:56px;display:flex;align-items:center;gap:20px;font-family:'Poppins',sans-serif;font-size:16px;color:var(--white)}
.contact-line svg{width:14px;height:14px}
.contact-email{top:444px}
.contact-web{top:470px}
.back-brand{position:absolute;left:574px;top:48px;font-family:'Oswald',sans-serif;font-weight:600;font-size:22px;line-height:1;color:var(--black);text-transform:uppercase}
.stamp{position:absolute;left:691px;top:30px;width:84px;height:84px;background:var(--stamp)}
</style>
</head>
<body>

<section class="card card-front">
  <svg class="shapes" viewBox="0 0 810 525" aria-hidden="false">
    <defs>
      <linearGradient id="roofPhoto" x1="0" y1="0" x2="0" y2="1">
        <stop offset="0" stop-color="#3a3b3d"/>
        <stop offset="0.35" stop-color="#5a5650"/>
        <stop offset="0.6" stop-color="#c9a470"/>
        <stop offset="1" stop-color="#b08a55"/>
      </linearGradient>
    </defs>
    <polygon points="385,0 408,0 525,250 458,415 435,415 502,250" fill="var(--stripe)"/>
    <polygon points="345,0 385,0 502,250 435,415 400,415 465,250" fill="var(--yellow)"/>
    <polygon points="408,0 810,0 810,415 458,415 525,250" fill="url(#roofPhoto)" role="img" aria-label="Photo of a roofer in a cap and work overalls installing shingles on a roof"/>
    <polygon points="0,150 417,150 466,254 0,254" fill="var(--black)"/>
    <polygon points="0,254 468,254 425,352 0,352" fill="var(--yellow)"/>
    <polygon points="0,441 425,441 395,525 0,525" fill="var(--black)"/>
    <polygon points="455,415 810,415 810,525 418,525" fill="var(--yellow)"/>
  </svg>

  <div class="brand">
    <div class="brand-dot"></div>
    <div class="brand-name">Olum<br>Roofing</div>
  </div>

  <h1 class="headline headline-stop">Stop the</h1>
  <div class="headline headline-knock">Knocking!</div>

  <p class="tagline">Tired of roofers<br>knocking on your door?</p>

  <div class="phone front-phone">
    <svg viewBox="0 0 36 36"><circle cx="18" cy="18" r="18" fill="var(--yellow)"/><path d="M12 9c1-1 2-1 3 0l2 3c.6 1 .4 2-.4 2.6l-1.2 1c.9 2.2 2.6 4 4.8 5l1-1.3c.7-.8 1.7-1 2.6-.4l3 2c1 .7 1 2 0 3l-1.6 1.6c-1.5 1.5-5 .6-8.6-3S10 13 11.5 11.5z" fill="var(--black)"/></svg>
    <span>877.612.OLUM</span>
  </div>

  <p class="value-note">Contact us because we value<br>your time as much as you value<br>the roof over your head.</p>
</section>

<section class="card card-back">
  <svg class="shapes" viewBox="0 0 810 525">
    <polygon points="392,0 418,0 536,254 436,525 410,525 510,254" fill="var(--stripe)"/>
    <polygon points="352,0 392,0 510,254 410,525 370,525 470,254" fill="var(--yellow)"/>
    <polygon points="0,252 469,252 423,382 0,382" fill="var(--yellow)"/>
    <polygon points="0,382 423,382 370,525 0,525" fill="var(--black)"/>
  </svg>

  <h2 class="contact-title">Contact <span>Olum</span></h2>

  <div class="work-grid">
    <div class="work-tile tile-a" role="img" aria-label="Photo of a house with new roof framing"></div>
    <div class="work-tile tile-b" role="img" aria-label="Photo of a roof covered with blue tarp"></div>
    <div class="work-tile tile-c" role="img" aria-label="Photo of a finished gable roof"></div>
    <div class="work-tile tile-d" role="img" aria-label="Photo of close-up roof shingles"></div>
    <div class="work-tile tile-e" role="img" aria-label="Photo of roofers working on a roof"></div>
    <div class="work-tile tile-f" role="img" aria-label="Photo of a roof under repair from above"></div>
  </div>

  <p class="caption">From inspection to installation,<br>OLUM has you covered.</p>

  <div class="phone back-phone">
    <svg viewBox="0 0 36 36"><circle cx="18" cy="18" r="18" fill="var(--yellow)"/><path d="M12 9c1-1 2-1 3 0l2 3c.6 1 .4 2-.4 2.6l-1.2 1c.9 2.2 2.6 4 4.8 5l1-1.3c.7-.8 1.7-1 2.6-.4l3 2c1 .7 1 2 0 3l-1.6 1.6c-1.5 1.5-5 .6-8.6-3S10 13 11.5 11.5z" fill="var(--black)"/></svg>
    <span>877.612.OLUM</span>
  </div>

  <div class="contact-line contact-email">
    <svg viewBox="0 0 14 14"><rect x="1" y="3" width="12" height="8" fill="none" stroke="var(--yellow)" stroke-width="1.3"/><path d="M1 3l6 5 6-5" fill="none" stroke="var(--yellow)" stroke-width="1.3"/></svg>
    <span>info@olumroofing.com</span>
  </div>
  <div class="contact-line contact-web">
    <svg viewBox="0 0 14 14"><circle cx="7" cy="7" r="6" fill="none" stroke="var(--yellow)" stroke-width="1.2"/><ellipse cx="7" cy="7" rx="2.6" ry="6" fill="none" stroke="var(--yellow)" stroke-width="1.1"/><path d="M1 7h12" stroke="var(--yellow)" stroke-width="1.1"/></svg>
    <span>OlumRoofing.com</span>
  </div>

  <div class="back-brand">Olum<br>Roofing</div>
  <div class="stamp"></div>
</section>

</body>
</html>
```